Business Card Design Project

TRK Solutions is a Electrical and Communications Services and Maintenance contractor to the Mining Oil and Gas sectors of Australia.
Our clients will be planners, Schedulers, Tradespeople and Engineers

We are yet to determine the primary colours that we will use on the business cards but the logos attached will form foundation of the colours used for logos on Business cards, Website, Uniforms, vehicles etc.

Target Market(s)

Mining engineers and shedulers

Industry/Entity Type

Contractor

Requirements
Must have
• information to be included on the card

Name: Derek Hanley
Title: Managing Director
Company: TRK Solutions Pty Ltd
Phone: 08 9YYY YYYY
Mobile 0400 813 942
email: dhanley@trksolutions-example.com
Website www.trksolutions-example.com

Address: U5/7 Bexley Street Kelvale, QX 4820
Postal Address: PO Box 4187 Kelvale QX 4821

Nice to have
• Double sided. Maybe the logo on the back

```html
<!DOCTYPE html>
<html lang="en">
<head>
<meta charset="utf-8">
<title>TRK Solutions – Business Card</title>
<link href="https://fonts.googleapis.com/css2?family=Arimo:wght@400;700&display=swap" rel="stylesheet">
<style>
  :root {
    --ink: #000000;
    --paper: #ffffff;
    --band: #0d0d0d;
    --orange-light: #fdb44c;
    --orange-mid: #f9a23a;
    --orange-deep: #f36f1f;
    --rule: #fcd9a8;
    --scene: rgba(214, 110, 20, 0.28);
  }
  * { margin: 0; padding: 0; box-sizing: border-box; }
  html, body {
    width: 1200px; height: 900px; overflow: hidden;
    background: var(--paper);
    font-family: "Arimo", Arial, sans-serif;
  }
  .sheet { position: relative; width: 1200px; height: 900px; }

  .side-label { position: absolute; font-size: 26px; color: var(--ink); font-weight: 400; }
  .side-label--front { left: 301px; top: 12px; }
  .side-label--back { left: 296px; top: 481px; }

  .card {
    position: absolute; width: 616px; height: 352px; overflow: hidden;
    background: linear-gradient(180deg, var(--orange-light) 0%, var(--orange-mid) 45%, var(--orange-deep) 100%);
  }
  .card--front { left: 291px; top: 52px; }
  .card--back {
    left: 287px; top: 519px;
    background: linear-gradient(180deg, var(--orange-mid) 0%, var(--orange-light) 55%, var(--orange-mid) 100%);
  }

  .band { position: absolute; left: 0; width: 100%; background: var(--band); }
  .band--top-front { top: 0; height: 63px; border-bottom: 3px solid var(--rule); }
  .band--top-back { top: 0; height: 24px; border-bottom: 3px solid var(--rule); }
  .band--bottom-back { bottom: 0; height: 26px; border-top: 3px solid var(--rule); }

  .company-line {
    position: absolute; top: 10px; width: 100%; text-align: center;
    color: var(--paper); font-weight: 700; font-size: 27px;
  }

  .wordmark {
    position: absolute; left: 0; width: 100%;
    display: flex; align-items: center; justify-content: center; gap: 14px;
    color: var(--band); font-weight: 700; font-size: 52px; letter-spacing: 1px;
  }
  .wordmark__square { width: 22px; height: 22px; background: var(--band); }
  .card--front .wordmark { top: 82px; }
  .card--back .wordmark { top: 146px; }

  .person { position: absolute; top: 200px; width: 100%; text-align: center; color: var(--ink); }
  .person__name { font-size: 26px; line-height: 30px; }
  .person__title { font-size: 17px; line-height: 22px; }

  .divider { position: absolute; left: 16px; right: 19px; top: 292px; height: 2px; background: var(--rule); }

  .contact { position: absolute; top: 299px; color: var(--paper); font-size: 18px; line-height: 25px; white-space: nowrap; }
  .contact--phones { left: 19px; }
  .contact--address { right: 20px; text-align: right; }

  .scene {
    position: absolute; top: 27px; height: 297px; width: 148px;
    background: radial-gradient(ellipse at 50% 55%, var(--scene) 0%, rgba(214,110,20,0.12) 55%, rgba(214,110,20,0) 80%);
  }
  .scene--left { left: 10px; }
  .scene--right { right: 10px; }

  .web-line { position: absolute; width: 100%; text-align: center; color: var(--paper); white-space: nowrap; }
  .web-line--email { top: 78px; font-size: 21px; }
  .web-line--site { top: 250px; font-size: 25px; }
  .web-line__bar { margin: 0 10px; }
</style>
</head>
<body>
<main class="sheet">
  <p class="side-label side-label--front">Front</p>
  <section class="card card--front">
    <div class="band band--top-front"></div>
    <h1 class="company-line">TRK Solutions Pty Ltd</h1>
    <div class="wordmark"><span>TRK Solutions</span><span class="wordmark__square"></span></div>
    <div class="person">
      <p class="person__name">Derek Hanley</p>
      <p class="person__title">Managing Director</p>
    </div>
    <div class="divider"></div>
    <div class="contact contact--phones">
      <p>Ph: 08 9YYY YYYY</p>
      <p>M:&nbsp; 0400 813 942</p>
    </div>
    <div class="contact contact--address">
      <p>U5/7 Bexley Street Kelvale, QX 4820</p>
      <p>PO Box 4187 Kelvale QX 4821</p>
    </div>
  </section>

  <p class="side-label side-label--back">Back</p>
  <section class="card card--back">
    <div class="band band--top-back"></div>
    <div class="scene scene--left" role="img" aria-label="Faint silhouette of an oil pump jack with a standing worker in a hard hat"></div>
    <div class="scene scene--right" role="img" aria-label="Faint silhouette of an oil pump jack with a standing worker in a hard hat"></div>
    <p class="web-line web-line--email"><span class="web-line__bar">|</span>dhanley@trksolutions-example.com<span class="web-line__bar">|</span></p>
    <div class="wordmark"><span>TRK Solutions</span><span class="wordmark__square"></span></div>
    <p class="web-line web-line--site"><span class="web-line__bar">|</span>www.trksolutions-example.com<span class="web-line__bar">|</span></p>
    <div class="band band--bottom-back"></div>
  </section>
</main>
</body>
</html>
```